PeerLoop Background Image Needed

I need a PeerLoop background image for my personal PeerLoop profile page. The dimension is 1400 pixels wide X 350 pixels high.

I am a consultant for www.TallOrangeLeap.com. The logo files are located here:

https://www.filecratio.net/shr/fd/m8tq2wxe7ulpa3vzrcoyn/k?akey=pq4nwc7udtr2ghwkmxbe81ys3&vw=0

A single message in the background is:

"Give your business a Tall Orange Leap with a proven path to optimized sales"

```html
<!DOCTYPE html>
<html lang="en">
<head>
<meta charset="utf-8">
<title>Tall Orange Leap – Profile Banner</title>
<link href="https://fonts.googleapis.com/css2?family=Poppins:ital,wght@1,800&display=swap" rel="stylesheet">
<style>
  :root {
    --page-bg: #ffffff;
    --banner-navy: #1b2230;
    --banner-navy-deep: #141a26;
    --headline-blue: #1f86c4;
    --headline-orange: #f0521f;
    --headline-white: #ffffff;
    --visual-glow: #2f6fc0;
    --visual-shadow: #16203a;
  }
  * { margin: 0; padding: 0; box-sizing: border-box; }
  html, body {
    width: 1028px;
    height: 1200px;
    overflow: hidden;
    background: var(--page-bg);
  }
  .canvas {
    position: relative;
    width: 1028px;
    height: 1200px;
  }
  .profile-banner {
    position: absolute;
    left: 34px;
    top: 480px;
    width: 960px;
    height: 240px;
    background: linear-gradient(100deg, var(--banner-navy-deep) 0%, var(--banner-navy) 55%, var(--banner-navy-deep) 100%);
    overflow: hidden;
    font-family: "Poppins", sans-serif;
    font-style: italic;
    font-weight: 800;
  }
  .brand-mark {
    position: absolute;
    left: 28px;
    top: 36px;
    display: flex;
    align-items: center;
    gap: 10px;
  }
  .brand-mark__dot {
    width: 46px;
    height: 46px;
    border-radius: 50%;
    background: var(--headline-orange);
    flex-shrink: 0;
  }
  .brand-mark__name {
    color: var(--headline-white);
    font-size: 19px;
    line-height: 19px;
    text-transform: uppercase;
    letter-spacing: -0.3px;
  }
  .headline {
    position: absolute;
    left: 237px;
    top: 38px;
    text-transform: uppercase;
    letter-spacing: -0.6px;
  }
  .headline__line { display: block; white-space: nowrap; }
  .headline__line--lead {
    color: var(--headline-blue);
    font-size: 31px;
    line-height: 36px;
  }
  .headline__line--brand {
    color: var(--headline-orange);
    font-size: 38px;
    line-height: 46px;
  }
  .headline__line--promise {
    color: var(--headline-white);
    font-size: 30px;
    line-height: 33px;
  }
  .headline__line--promise:first-of-type { margin-top: 0; }
  .growth-visual {
    position: absolute;
    left: 650px;
    top: 0;
    width: 310px;
    height: 240px;
    background:
      radial-gradient(ellipse at 55% 30%, var(--visual-glow) 0%, rgba(47,111,192,0.35) 35%, transparent 70%),
      radial-gradient(ellipse at 50% 85%, var(--visual-shadow) 0%, transparent 70%);
  }
</style>
</head>
<body>
  <main class="canvas">
    <section class="profile-banner">
      <div class="brand-mark">
        <span class="brand-mark__dot"></span>
        <span class="brand-mark__name">Tall<br>Orange<br>Leap</span>
      </div>
      <h1 class="headline">
        <span class="headline__line headline__line--lead">Give your business</span>
        <span class="headline__line headline__line--brand">A Tall Orange Leap</span>
        <span class="headline__line headline__line--promise">With a proven path</span>
        <span class="headline__line headline__line--promise">to optimized sales</span>
      </h1>
      <div class="growth-visual" role="img" aria-label="Hand holding a smartphone with a glowing rising bar chart and upward arrow"></div>
    </section>
  </main>
</body>
</html>
```